Fundraiser Flyer and Email Template

We are looking for a flexible coordinated flyer and email template. The feel of both should be more formal or professional. We are not looking for an overly "political" design that features American flags or other "political" symbols.

We are a political fundraising firm that works with elected officials to set up fundraisers for their campaigns. We send the invites to these events via US Mail and email, so we are looking for a standardized template that will work as both an 8.5 x 11 inch printed flyer, as well as an email template.

The information in the email will be text, but images can be used for formatting.

Some clients have a campaign logo, others do not. The format should be flexible enough to either include the logo, or leave it out. Size also varies.

Any colors in the template should be editable so we can match logos as we get them.

We're open to any format that allows us to edit the format as needed. This would include Photoshop, Microsoft Word, etc.

The text of the invite should include space for:

---------------------------------------
NAME
DISTRICT NUMBER AND OFFICE

DATE OF EVENT
TIME OF EVENT

LOCATION
LOCATION ADDRESS
LOCATION CITY, STATE, ZIP

SUGGESTED CONTRIBUTION LEVELS (Typically 3 levels are provided such as Gold: $1,000, Silver: $500, Bronze: $250)

ADDRESS TO SEND CHECKS TO

RSVP CONTACT INFORMATION

The invite will also need fine-print at the bottom that reads:
"Pennsylvania law allows personal, partnership, and PAC contributions. By law we cannot accept corporate contributions
Paid for by [NAME]"

Industry/Entity Type

It Professional

Font styles to use
Serif
Sans Serif

Requirements
Must have
• Must have spaces for:
• NAME
• DISTRICT NUMBER AND OFFICE
• DATE OF EVENT
• TIME OF EVENT
• LOCATION
• LOCATION ADDRESS
• LOCATION CITY, STATE, ZIP
• SUGGESTED CONTRIBUTION LEVELS (Typically 3 levels are provided such as Gold: $1,000, Silver: $500, Bronze: $250)
• ADDRESS TO SEND CHECKS TO
• RSVP CONTACT INFORMATION
• The invite will also need fine-print at the bottom that reads:
• "Pennsylvania law allows personal, partnership, and PAC contributions. By law we cannot accept corporate contributions
• Paid for by [NAME]"
Should not have
• It should not be overly "political".

```html
<!DOCTYPE html>
<html lang="en">
<head>
<meta charset="utf-8">
<title>Fundraiser Flyer</title>
<link rel="stylesheet" href="https://fonts.googleapis.com/css2?family=Bebas+Neue&family=Roboto:wght@400&display=swap">
<style>
  :root {
    --ink: #1c1c1e;
    --ink-deep: #121214;
    --silver-light: #f2f2f2;
    --silver-mid: #cfcfcf;
    --accent: #0aa3e2;
    --accent-text: #1ba7e6;
    --white: #ffffff;
    --text-dark: #222226;
    --divider: #8c86d8;
    --gold: #e2c25a;
    --silver-tone: #d8d8d8;
    --bronze: #c79a6a;
    --fine-print: #dcdcdc;
  }
  * { margin: 0; padding: 0; box-sizing: border-box; }
  html, body { width: 950px; height: 1200px; overflow: hidden; background: var(--ink); }
  .flyer {
    position: relative; width: 950px; height: 1200px; overflow: hidden;
    background: linear-gradient(180deg, #232325 0%, var(--ink-deep) 100%);
    font-family: "Bebas Neue", "Arial Narrow", sans-serif; color: var(--white);
  }
  .bands { position: absolute; inset: 0; }
  .title {
    position: absolute; top: 52px; left: 0; width: 100%; text-align: center;
    font-size: 128px; letter-spacing: 4px; line-height: 1;
    background: linear-gradient(180deg, #fff6cf 0%, #d8b756 45%, #8a6a22 55%, #e8cf7a 100%);
    -webkit-background-clip: text; background-clip: text; color: transparent;
    filter: drop-shadow(0 4px 4px rgba(0,0,0,.7));
  }
  .district {
    position: absolute; top: 198px; left: 0; width: 100%; text-align: center;
    font-size: 54px; letter-spacing: 1px;
  }
  .tag {
    position: absolute; background: var(--ink); color: var(--white);
    font-size: 58px; letter-spacing: 2px; display: flex; align-items: center; justify-content: center;
    transform: rotate(-5.5deg); border-radius: 6px; box-shadow: 0 3px 6px rgba(0,0,0,.35);
  }
  .tag-date { left: -20px; top: 420px; width: 490px; height: 84px; padding-left: 40px; }
  .tag-time { left: 488px; top: 362px; width: 490px; height: 84px; padding-right: 40px; }
  .location {
    position: absolute; top: 538px; left: 0; width: 100%;
    display: flex; flex-direction: column; align-items: center;
    color: var(--text-dark); font-size: 38px; line-height: 1;
  }
  .location-line { padding: 6px 0; }
  .location-divider { width: 420px; height: 1px; background: var(--divider); margin: 3px 0; }
  .contributions {
    position: absolute; top: 718px; left: 0; width: 100%; text-align: center;
  }
  .contributions-heading { font-size: 52px; color: var(--accent-text); letter-spacing: 1px; line-height: 1; }
  .contributions-note { font-size: 30px; line-height: 1; margin-top: 6px; }
  .levels { font-size: 36px; line-height: 1; margin-top: 8px; }
  .level-gold { color: var(--gold); }
  .level-silver { color: var(--silver-tone); }
  .level-bronze { color: var(--bronze); }
  .level-sep { color: var(--white); margin: 0 10px; }
  .mailing {
    position: absolute; top: 898px; left: 0; width: 100%; text-align: center;
    font-size: 42px; line-height: 1.3; letter-spacing: .5px;
  }
  .fine-print {
    position: absolute; left: 42px; top: 1064px; width: 866px; height: 112px;
    border: 1.5px dashed var(--accent); border-radius: 18px;
    display: flex; align-items: center; justify-content: center; text-align: center;
    font-family: "Roboto", Arial, sans-serif; font-size: 21px; line-height: 1.4; color: var(--fine-print);
    padding: 0 24px;
  }
</style>
</head>
<body>
<main class="flyer">
  <svg class="bands" width="950" height="1200" viewBox="0 0 950 1200" aria-hidden="true">
    <defs>
      <linearGradient id="silver" x1="0" y1="0" x2="1" y2="1">
        <stop offset="0" stop-color="#d9d9d9"/>
        <stop offset=".5" stop-color="#f4f4f4"/>
        <stop offset="1" stop-color="#c6c6c6"/>
      </linearGradient>
    </defs>
    <polygon class="band-silver" points="0,261 475,328 950,261 950,682 475,705 0,682" fill="url(#silver)"/>
    <polyline points="0,261 475,328 950,261" fill="none" stroke="var(--accent)" stroke-width="9"/>
    <polyline points="0,682 475,705 950,682" fill="none" stroke="var(--divider)" stroke-width="2"/>
    <polygon class="band-accent" points="0,842 475,868 950,842 950,1006 475,1033 0,1006" fill="var(--accent)"/>
    <polyline points="0,838 475,864 950,838" fill="none" stroke="#d7d7e6" stroke-width="5"/>
    <polyline points="0,1010 475,1037 950,1010" fill="none" stroke="#d7d7e6" stroke-width="5"/>
  </svg>

  <h1 class="title">The Event</h1>
  <p class="district">District Number and Office</p>

  <div class="tag tag-date">Date of Event</div>
  <div class="tag tag-time">Time of Event</div>

  <div class="location">
    <span class="location-line">Location Goes Here</span>
    <span class="location-divider"></span>
    <span class="location-line">Location Address Goes Here</span>
    <span class="location-divider"></span>
    <span class="location-line">Location City, State, Zip</span>
  </div>

  <section class="contributions">
    <h2 class="contributions-heading">Suggested Contribution Levels</h2>
    <p class="contributions-note">(Typically 3 levels are provided such as</p>
    <p class="levels">
      <span class="level-gold">Gold: $1,000</span><span class="level-sep">|</span><span class="level-silver">Silver: $500</span><span class="level-sep">|</span><span class="level-bronze">Bronze: $250</span>)
    </p>
  </section>

  <section class="mailing">
    <p>Address to send checks to_ goes here</p>
    <p>RSVP contact information_ goes here</p>
  </section>

  <footer class="fine-print">"Pennsylvania law allows personal, partnership, and PAC contributions. By law we cannot accept corporate contributions Paid for by [NAME]</footer>
</main>
</body>
</html>
```